Event Poster for Bar Sunday Live Music and Happy Hour

We are a bar. Every Sunday we have a HARBOUR HOURS event where we have live music and a Sunday Happy Hour. I would like a poster that promotes this weekly event in A4 and A3. Information the poster should include:Event Name: SUNDAY SESSIONSVenue: Copper Lantern 218-222 Marlow Rd PrestonDrink Specials: 3:00 pm - 5:00pmLive Music: 4:30pm -6:30pmAttached is our logo.

Target Market(s)

Both sexes 30-40 year olds

Industry/Entity Type

Hospitality

Font styles to use
Sans Serif

Colors

Designer to choose colors to be used in the design.

Requirements
Must have
• Event Name: HARBOUR HOURS
• Venue: Copper Lantern 218-222 Marlow Rd Preston
• Drink Specials: 3:00 pm - 5:00pm
• Live Music: 4:30pm -6:30pm
• Logo
Nice to have
• Open to different styles and ideas. Like colour.
Should not have
• It should not be too blokey are over the top bar-like.

```html
<!DOCTYPE html>
<html lang="en">
<head>
<meta charset="utf-8">
<title>Harbour Hours – Copper Lantern</title>
<link rel="stylesheet" href="https://fonts.googleapis.com/css2?family=Inter:wght@600;700;800&display=swap">
<style>
  :root {
    --backdrop: #e9e6ee;
    --mustard: #e3a82e;
    --blush: #ebbdbd;
    --teal: #5db3a0;
    --chalk: #f2efe9;
    --ink: #3b4663;
    --charcoal: #1f1f1f;
  }
  html, body {
    margin: 0;
    width: 1200px;
    height: 1200px;
    overflow: hidden;
    background: var(--backdrop);
  }
  .poster {
    position: absolute;
    left: 190px;
    top: 23px;
    width: 820px;
    height: 1154px;
    box-shadow: 0 6px 24px rgba(40, 35, 60, 0.18);
  }
  .poster text { font-family: "Inter", Helvetica, Arial, sans-serif; }
  .bg-mustard { fill: var(--mustard); }
  .wave-blush { fill: var(--blush); }
  .wave-teal { fill: var(--teal); }
  .music-title { fill: var(--teal); font-weight: 700; font-size: 86px; letter-spacing: -1px; }
  .music-time { fill: var(--teal); font-weight: 700; font-size: 54px; letter-spacing: -1px; }
  .event-name { fill: var(--chalk); font-weight: 800; font-size: 112px; letter-spacing: -2px; }
  .drinks-title { fill: var(--blush); font-weight: 700; font-size: 52px; letter-spacing: -0.5px; }
  .drinks-time { fill: var(--blush); font-weight: 700; font-size: 34px; letter-spacing: -0.5px; }
  .venue { fill: var(--ink); font-weight: 700; font-size: 19px; }
  .brand-dot { fill: var(--charcoal); }
  .brand-name { fill: var(--charcoal); font-weight: 700; font-size: 20px; }
</style>
</head>
<body>
  <svg class="poster" viewBox="0 0 877 1234" xmlns="http://www.w3.org/2000/svg" aria-label="Harbour Hours poster">
    <rect class="bg-mustard" x="0" y="0" width="877" height="1234"/>

    <path class="wave-blush" d="M760,0 H877 V92 H809 A44,44 0 0 0 809,180 H877 V690
      C850,620 800,568 700,568 H376 A160,160 0 0 1 376,248 H625 A34,34 0 0 0 625,180
      H570 A44,44 0 0 1 570,92 H700 A60,60 0 0 0 760,32 Z"/>

    <path class="wave-teal" d="M0,750 C0,830 60,894 150,894 H433 A87,87 0 0 1 433,1067
      H350 A45,45 0 0 0 350,1157 H600 A45,45 0 0 1 645,1202 V1234 H0 Z"/>
    <path class="bg-mustard" d="M0,1157 H265 A45,45 0 0 1 310,1202 V1234 H0 Z"/>

    <text class="music-title" x="353" y="400">Live Music</text>
    <text class="music-time" x="353" y="469">4:30pm - 6:30pm</text>

    <text class="event-name" x="65" y="715">HARBOUR</text>
    <text class="event-name" x="808" y="824" text-anchor="end">HOURS</text>

    <text class="drinks-title" x="65" y="970">Drink Specials</text>
    <text class="drinks-time" x="65" y="1025">3:00pm - 5:00pm</text>

    <text class="venue" x="350" y="1104">Copper Lantern</text>
    <text class="venue" x="350" y="1128">218-222 Marlow Rd Preston</text>

    <g class="brand">
      <circle class="brand-dot" cx="740" cy="1040" r="34"/>
      <text class="brand-name" x="740" y="1106" text-anchor="middle">Copper Lantern</text>
    </g>
  </svg>
</body>
</html>
```